Website Design For our Tour Company

We need a face lift on our current website. I want it to look the best! Lots of videos. An easy to use website to obtain easy conversions. I want people to feel like they are on the tour just by looking at our website. My current website is just bland and unprofessional looking. I want it to be incredibly mobile friendly and look great on the desk top. Our current website is https://www.halvorsenelitejaunts.example/
I would like there to be an option where the viewer can select what language they would like to read in. Im hoping you can pull a-lot of media and videos from out lumenfeed page. Im not happy with most of my descriptions for the product and tours we offer. Looking for professional help.

Our two main activities are Summer and Winter Tours
In The Summer the main things we do our Jet Boat & Jet Ski Tours.

In The Winter our main tour is luxury first class Aurora Viewing. I Would like to see a-lot of aurora video/photos as I believe that gets peoples attention!

Target Market(s)

Travelers from china and around the world

Coding

Coded - Design and coding required

Number of Pages Required

5+ page

Requirements
Must have
• be able to select what when language you would like to read the website in.
Nice to have
• The overall look and feel I want for the website is luxury, fancy, royalty. Think Harold Pemberly. I like the Luxury gold colors. I need the website to look ridiculously professional

incorporate Lots of Aurora photos / videos as one of our main tours is Aurora

```html
<!DOCTYPE html>
<html lang="en">
<head>
<meta charset="utf-8">
<title>Halvorsen Elite Jaunts</title>
<link rel="stylesheet" href="https://fonts.googleapis.com/css2?family=Noto+Sans:wght@400;500&family=Oswald:wght@300;400&family=Anton&family=Archivo+Black&family=Cutive+Mono&display=swap">
<style>
:root{
  --ink:#111;
  --grey:#5b5b5b;
  --white:#fff;
  --black:#000;
  --gold:#c9a85a;
  --sea-top:#3e5a5e;
  --sea-mid:#6e8c8f;
  --sea-deep:#123540;
  --panel:rgba(40,40,40,.82);
  --dusk-a:#d98a2c;
  --dusk-b:#8a4a17;
  --dusk-dark:#3a2210;
  --accent-red:#d0164a;
  --accent-blue:#1f2fd8;
}
*{margin:0;padding:0;box-sizing:border-box}
html,body{width:779px;height:1200px;overflow:hidden;background:var(--white)}
body{position:relative;font-family:"Noto Sans",sans-serif;color:var(--ink)}
.abs{position:absolute}

/* hero */
.hero{left:0;top:0;width:518px;height:323px;background:linear-gradient(180deg,var(--sea-top) 0%,var(--sea-mid) 30%,#2f5257 65%,var(--sea-deep) 100%)}
.hero-bar{left:0;top:0;width:518px;height:44px;background:rgba(40,70,72,.7)}
.hero-title{left:8px;top:9px;font-family:"Cutive Mono",monospace;font-size:17px;color:var(--white);letter-spacing:.5px}
.hero-tag{right:10px;top:24px;font-family:"Cutive Mono",monospace;font-size:9px;color:#e5e5e5}
.contact{left:0;top:54px;width:239px;height:205px;background:var(--panel)}
.contact h1{position:absolute;left:11px;top:6px;font-family:"Anton",sans-serif;font-weight:400;font-size:23px;color:var(--white)}
.field{position:absolute;left:14px;font-family:"Archivo Black",sans-serif;color:#ddd}
.field.name{top:41px;font-size:9px}
.field.mail{top:73px;font-size:9px}
.field.msg{top:111px;font-size:5px}
.submit{position:absolute;left:0;width:239px;top:181px;text-align:center;font-family:"Archivo Black",sans-serif;font-size:15px;color:var(--white)}
.lang{left:370px;top:285px;width:148px;height:29px;background:var(--white);border-radius:5px 0 0 5px;display:flex;align-items:center;padding-left:22px;font-size:13px}
.lang svg{position:absolute;left:107px;top:5px}

/* sidebar */
.brand-block{left:518px;top:0;width:261px;height:110px;background:var(--black);display:flex;align-items:center;justify-content:center;gap:10px}
.brand-mark{width:22px;height:22px;background:var(--gold)}
.brand-name{font-family:"Noto Sans",sans-serif;font-weight:500;color:var(--gold);font-size:17px;letter-spacing:1px}
.side-head{left:518px;width:261px;text-align:center;font-weight:400}
.side-menu{left:570px;top:165px;list-style:none;font-size:14px}
.side-menu li{height:35.6px}
.side-social{left:572px;top:442px;list-style:none;font-size:17px}
.side-social li{height:42px}
.side-more{left:577px;top:630px;list-style:none;font-size:13.5px}
.side-more li{height:33px}

/* deals */
.deals-title{left:0;width:518px;top:357px;text-align:center;font-size:17px;color:var(--grey);letter-spacing:.3px}
.card{top:409px;width:125px;height:146px;background:var(--white);box-shadow:0 1px 3px rgba(0,0,0,.3)}
.card .photo{height:83px}
.card h3{position:absolute;top:89px;width:100%;text-align:center;font-weight:400;font-size:10.5px;color:#333}
.card span{position:absolute;top:131px;width:100%;text-align:center;font-size:6px;color:#333}

/* intro */
.trip-title{left:0;width:518px;top:580px;text-align:center;font-family:"Oswald",sans-serif;font-weight:300;font-size:26px;letter-spacing:-.5px}
.logo-square{left:16px;top:626px;width:140px;height:140px;background:var(--black);display:flex;align-items:center;justify-content:center;gap:6px}
.logo-square .brand-name{font-size:11px;letter-spacing:.5px}
.logo-square .brand-mark{width:12px;height:12px}
.intro-copy{left:188px;top:632px;width:305px;font-size:10.4px;line-height:12.5px;color:var(--grey)}
.call{left:341px;top:751px;font-size:10.5px;color:var(--accent-red)}
.call em{font-style:normal;font-size:8px;color:var(--accent-blue);margin-left:3px}

/* about */
.about{left:0;top:793px;width:518px;height:134px;background:linear-gradient(180deg,#6a3c18 0%,var(--dusk-dark) 40%,#4a2c12 75%,#2a1609 100%)}
.about-side{left:0;top:793px;width:147px;height:134px;background:linear-gradient(180deg,#c9782a 0%,#8e5220 40%,var(--dusk-a) 60%,var(--dusk-b) 100%)}
.about h2{position:absolute}
.about-label{left:22px;top:842px;font-size:28px;font-weight:400;color:var(--white)}
.about-copy{left:158px;font-family:"Oswald",sans-serif;font-weight:300;font-size:8.4px;color:#f1e6d8;letter-spacing:-.2px;white-space:nowrap}

/* footer */
.foot-menu{left:29px;top:970px;list-style:none;font-size:13.5px}
.foot-menu li{height:33px}
.foot-social{left:161px;top:970px;list-style:none;font-size:15.5px}
.foot-social li{height:38px}
.foot-brand{left:313px;top:1131px;width:211px;height:58px;background:var(--black);display:flex;align-items:center;justify-content:center;gap:8px}
.foot-brand .brand-name{font-size:13px}
.foot-brand .brand-mark{width:14px;height:14px}
</style>
</head>
<body>

<section class="abs hero" role="img" aria-label="Photo of a rider on a jet ski spraying across open sea"></section>
<div class="abs hero-bar"></div>
<div class="abs hero-title">HALVORSEN ELITE JAUNTS</div>
<div class="abs hero-tag">Taking you, Where you want to go</div>

<form class="abs contact">
  <h1>Contact us</h1>
  <div class="field name">Name</div>
  <div class="field mail">E-mail</div>
  <div class="field msg">your message goes here...</div>
  <div class="submit">Submit</div>
</form>

<div class="abs lang">English
  <svg width="24" height="20" viewBox="0 0 24 20"><rect y="0" width="24" height="4" rx="2" fill="#000"/><rect y="8" width="24" height="4" rx="2" fill="#000"/><rect y="16" width="24" height="4" rx="2" fill="#000"/></svg>
</div>

<aside>
  <div class="abs brand-block"><span class="brand-mark"></span><span class="brand-name">HALVORSEN ELITE JAUNTS</span></div>
  <h2 class="abs side-head" style="top:114px;font-size:24px">Menu</h2>
  <ul class="abs side-menu">
    <li>Home</li><li>Summer Tours</li><li>Winter Tours</li><li>Car Rentals</li><li>Book online</li><li>Blog</li>
  </ul>
  <h2 class="abs side-head" style="top:390px;font-size:19px">Follow us</h2>
  <ul class="abs side-social"><li>Lumenfeed</li><li>Chirpline</li><li>Snapgrove</li></ul>
  <h2 class="abs side-head" style="top:576px;font-size:21px">More</h2>
  <ul class="abs side-more"><li>About us</li><li>Contact Number</li></ul>
</aside>

<h2 class="abs deals-title" style="font-weight:400">GREAT DEALS ON GUIDED TOURS</h2>

<article class="abs card" style="left:25px">
  <div class="photo" role="img" aria-label="Beach bag and sun hat on a towel by the sea" style="background:linear-gradient(180deg,#2aa6b8 0%,#7cc6c8 35%,#e6d2ae 60%,#d8bf96 100%)"></div>
  <h3>Summer Tours</h3><span>Begin Adventure</span>
</article>
<article class="abs card" style="left:199px">
  <div class="photo" role="img" aria-label="Snowy pine forest under a pink sunset sky" style="background:linear-gradient(180deg,#c9626a 0%,#e79a80 35%,#b9b6c8 60%,#eef0f4 100%)"></div>
  <h3>Winter Tours</h3><span>Begin Adventure</span>
</article>
<article class="abs card" style="left:370px">
  <div class="photo" role="img" aria-label="Silver full-size SUV parked by a canyon" style="background:linear-gradient(180deg,#9fb0c4 0%,#c9ccd1 45%,#8e9094 75%,#6c6a68 100%)"></div>
  <h3>Car Rentals</h3><span>Learn More</span>
</article>

<h2 class="abs trip-title">TAKE YOUR NEXT TRIP WITH</h2>
<div class="abs logo-square"><span class="brand-mark"></span><span class="brand-name">HALVORSEN</span></div>
<p class="abs intro-copy">Halvorsen Resorts, LLC specializes in providing the best travel services in Fairbanks, Alaska.<br>We’ve been in Fairbanks since 1995, creating customized itineraries for our clients based around their personal plans and preferences.<br>In our line of work we don’t only make plans, we help you build experiences and memories.<br>Let us arrange the details of your next trip.</p>
<div class="abs call">CALL TODAY<em>Your number goes here</em></div>

<section>
  <div class="abs about" role="img" aria-label="Rolling hills at golden dusk"></div>
  <div class="abs about-side" role="img" aria-label="Golden prairie at sunset"></div>
  <h2 class="abs about-label">ABOUT</h2>
  <div class="abs about-copy" style="top:803px">Great Journeys. Fascinating Places.</div>
  <div class="abs about-copy" style="top:828px">Local Experts Rowan, Lucia, and Everett</div>
  <div class="abs about-copy" style="top:879px">Everett - Life-long Alaskan - Local expert, loves the outdoors, construction, &amp; adventures</div>
  <div class="abs about-copy" style="top:892px">Rowan - Life-long Alaskan - Local expert entrepreneur, loves Alaska, always ready for an adventure and a fun time!</div>
  <div class="abs about-copy" style="top:905px">Lucia - Life-long Alaska - Local expert, company cook, organizes the activities &amp; schedule. Without her we have no organization.</div>
</section>

<footer>
  <ul class="abs foot-menu"><li>Home</li><li>Summer Tours</li><li>Winter Tours</li><li>Car Rentals</li><li>Book online</li><li>Blog</li></ul>
  <ul class="abs foot-social"><li>Lumenfeed</li><li>Chirpline</li><li>Snapgrove</li></ul>
  <div class="abs foot-brand"><span class="brand-mark"></span><span class="brand-name">HALVORSEN ELITE JAUNTS</span></div>
</footer>

</body>
</html>
```